Banner 34"x81"

This is for a Pull Up Banner
I am supplying a sample of my logo and some of my art work for you to incorporate into an upright banner.
Please business name:LuellaRo OpenHarbor Psychotherapy
phone number: 583-214-9067 NOT THE ONE ON THE BUSINESS CARD

```html
<!DOCTYPE html>
<html lang="en">
<head>
<meta charset="utf-8">
<title>LuellaRo OpenHarbor Psychotherapy – Pull Up Banner</title>
<link rel="stylesheet" href="https://fonts.googleapis.com/css2?family=Oswald:wght@600;700&family=Josefin+Sans:wght@200;300&display=swap">
<style>
  :root {
    --page-bg: #ffffff;
    --banner-dark: #1b222b;
    --photo-blue: #4a74c2;
    --photo-blue-light: #8aa8de;
    --photo-blue-deep: #3a62b0;
    --text-white: #ffffff;
    --text-grey: #e3e3e6;
    --accent-red: #e3141b;
  }
  * { margin: 0; padding: 0; box-sizing: border-box; }
  html, body {
    width: 1030px;
    height: 1200px;
    overflow: hidden;
    background: var(--page-bg);
  }
  .banner {
    position: absolute;
    left: 325px;
    top: 170px;
    width: 367px;
    height: 873px;
    background: var(--banner-dark);
    overflow: hidden;
  }
  .banner__header {
    position: absolute;
    left: 0;
    top: 0;
    width: 367px;
    height: 400px;
    display: block;
  }
  .banner__body {
    position: absolute;
    inset: 0;
    text-align: center;
    color: var(--text-white);
  }
  .brand-mark {
    position: absolute;
    left: 0;
    top: 420px;
    width: 100%;
    height: 60px;
    display: flex;
    align-items: center;
    justify-content: center;
    gap: 14px;
  }
  .brand-mark__square {
    width: 44px;
    height: 44px;
    border: 3px solid var(--text-white);
  }
  .brand-mark__name {
    font-family: "Oswald", sans-serif;
    font-weight: 600;
    font-size: 40px;
    line-height: 60px;
    color: var(--text-white);
  }
  .brand-name {
    position: absolute;
    left: 0;
    top: 516px;
    width: 100%;
    font-family: "Oswald", sans-serif;
    font-weight: 700;
    font-size: 38px;
    line-height: 50px;
    color: var(--text-white);
  }
  .practice-name {
    position: absolute;
    left: 0;
    top: 582px;
    width: 100%;
    font-family: "Josefin Sans", sans-serif;
    font-weight: 300;
    font-size: 42px;
    line-height: 50px;
    color: var(--text-white);
  }
  .practice-type {
    position: absolute;
    left: 0;
    top: 637px;
    width: 100%;
    font-family: "Oswald", sans-serif;
    font-weight: 600;
    font-size: 25px;
    line-height: 32px;
    letter-spacing: 2px;
    color: var(--text-grey);
  }
  .phone-icon {
    position: absolute;
    left: 160px;
    top: 697px;
    width: 47px;
    height: 47px;
  }
  .phone-number {
    position: absolute;
    left: 0;
    top: 760px;
    width: 100%;
    font-family: "Josefin Sans", sans-serif;
    font-weight: 200;
    font-size: 48px;
    line-height: 56px;
    letter-spacing: 1px;
    color: var(--text-white);
  }
</style>
</head>
<body>
  <main class="banner">
    <svg class="banner__header" viewBox="0 0 367 400" xmlns="http://www.w3.org/2000/svg">
      <defs>
        <radialGradient id="portraitTone" cx="0.45" cy="0.45" r="0.75">
          <stop offset="0" stop-color="var(--photo-blue-light)"/>
          <stop offset="0.55" stop-color="var(--photo-blue)"/>
          <stop offset="1" stop-color="var(--photo-blue-deep)"/>
        </radialGradient>
      </defs>
      <rect class="portrait-area" x="0" y="0" width="367" height="400" fill="url(#portraitTone)" role="img" aria-label="Portrait photo of the therapist in blue duotone, seated on a tufted leather chair"/>
      <polygon class="chevron-stripe" points="0,398 183.5,343 367,398 367,400 0,400" fill="var(--page-bg)"/>
      <polygon class="chevron-base" points="0,398 183.5,356 367,398 367,400 0,400" fill="var(--banner-dark)"/>
    </svg>

    <section class="banner__body">
      <div class="brand-mark">
        <span class="brand-mark__square"></span>
        <span class="brand-mark__name">LuellaRo</span>
      </div>
      <h1 class="brand-name">LuellaRo</h1>
      <p class="practice-name">OpenHarbor</p>
      <p class="practice-type">PSYCHOTHERAPY</p>
      <svg class="phone-icon" viewBox="0 0 62 62" xmlns="http://www.w3.org/2000/svg" aria-hidden="true">
        <circle cx="31" cy="31" r="28.5" fill="none" stroke="var(--accent-red)" stroke-width="2.5"/>
        <path d="M22 20c1.5-1.6 3.2-1.6 4.2 0l2.4 3.6c.8 1.2.5 2.4-.6 3.3l-1.4 1.1c1.2 2.8 3.6 5.3 6.4 6.6l1.2-1.4c.9-1.1 2.1-1.3 3.3-.5l3.6 2.4c1.6 1 1.5 2.8 0 4.2l-1.6 1.5c-1.6 1.5-4.4 1.4-7.4-.3-4.6-2.6-8.6-6.6-11.1-11.2-1.6-3-1.7-5.7-.2-7.3z" fill="none" stroke="var(--accent-red)" stroke-width="2" stroke-linejoin="round"/>
      </svg>
      <p class="phone-number">583-214-9067</p>
    </section>
  </main>
</body>
</html>
```